Help us make a CLOVERTON impact! Saving Dogs from Kill Shelters.....

*Our mission is to save Dogs from kill shelters, and unite them with responsible families nationwide.

*We would love to incorporate sacred geometry into our message. The "Flower of Life" needs to be incorporated into this design.Earth Friendly Self-Sustainable Animal Shelter is a goal. Solar Power

*We want the professional look of exclusiveness.

*The logo/brand is not set in stone, and we welcome opinions!

***Earth Consciousness. Awareness. Love.

Peace. LOVE. Adopt. :)

I would like a sleek exclusive look, one that says WOW. This design needs to have a good energy about it. I have envisioned the front being logo only and vertical. Please have a look at our Facebook page to get a feel about what we are doing & trying to accomplish...

*ONE Side Card
**The flower of life inlay needs to be in or around of the logo.
***The following is the ONLY information I want on the card!

CLOVERTON Adoption Center

Maren Hollis

www.CLOVERTONadoptioncenter.com

(555)013-4478

FB Icon

Target Market(s)

Stable, Wealthy, Responsible Families in the Northeast.

Industry/Entity Type

Solar

Contact Information for Business Card

CLOVERTON Adoption Center, Maren Hollis, Founder/Director, 912 Birchwood Court, Bath Springs, TN 40927, (555)013-4478, FB Icon

Requirements
Must have
• FB icon on back.
The "Flower of Life" must be incorporated into this design.
Nice to have
• Positive Energy
Bright Colors
WOW Factor

```html
<!DOCTYPE html>
<html lang="en">
<head>
<meta charset="utf-8">
<title>CLOVERTON Adoption Center – Business Card</title>
<link rel="stylesheet" href="https://fonts.googleapis.com/css2?family=Arimo:wght@400&family=Anton&display=swap">
<style>
  :root{
    --paper:#eefcfd;
    --frame:#c9cfd3;
    --lime:#7dea12;
    --lime-deep:#3aa80f;
    --leaf:#3a9e1e;
    --magenta:#f21ce0;
    --sun:#fff200;
    --orange:#ff8a00;
    --photo-light:#f6ecd6;
    --photo-mid:#e5c88f;
  }
  html,body{margin:0;padding:0;overflow:hidden;background:#ffffff;}
  .card{
    position:relative;width:702px;height:1200px;overflow:hidden;
    background:var(--paper);font-family:"Arimo",Arial,sans-serif;
  }
  .card__art{position:absolute;inset:0;}
  .puppy-photo{
    position:absolute;left:409px;top:0;width:293px;height:326px;
    background:radial-gradient(ellipse at 45% 40%,var(--photo-mid) 0%,var(--photo-light) 55%,rgba(246,236,214,0) 80%);
  }
  .brand{position:absolute;left:84px;top:80px;margin:0;}
  .brand__name{
    display:inline-block;font-size:50px;font-weight:400;color:var(--lime);
    letter-spacing:1px;line-height:1;
    text-shadow:2px 2px 0 var(--sun);
    border-bottom:4px solid var(--lime-deep);padding-bottom:2px;
  }
  .brand__tagline{display:block;font-size:33px;color:var(--leaf);margin-top:8px;line-height:1;}
  .person{
    position:absolute;left:82px;top:242px;margin:0;font-size:40px;font-weight:400;
    color:var(--magenta);text-shadow:2px 2px 0 var(--sun);
  }
  .contact{
    position:absolute;left:300px;top:998px;width:330px;text-align:center;
    font-family:"Anton",Impact,sans-serif;color:var(--lime);
    text-shadow:2px 2px 0 var(--orange);line-height:1.1;
  }
  .contact__name{font-size:42px;letter-spacing:1px;display:block;}
  .contact__phone{font-size:46px;display:block;}
</style>
</head>
<body>
<main class="card">
  <svg class="card__art" width="702" height="1200" viewBox="0 0 702 1200" aria-hidden="true">
    <defs>
      <radialGradient id="rainbow" cx="442" cy="884" r="600" gradientUnits="userSpaceOnUse">
        <stop offset="0" stop-color="#7df21a"/>
        <stop offset="0.22" stop-color="#b8f51a"/>
        <stop offset="0.45" stop-color="#f5f51a"/>
        <stop offset="0.7" stop-color="#fff200"/>
        <stop offset="0.76" stop-color="#ffb000"/>
        <stop offset="0.8" stop-color="#ff2a2a"/>
        <stop offset="0.84" stop-color="#e21ce8"/>
        <stop offset="0.88" stop-color="#3a4cf2"/>
        <stop offset="0.93" stop-color="#5fe8f5"/>
        <stop offset="1" stop-color="#eefcfd" stop-opacity="0"/>
      </radialGradient>
      <radialGradient id="orb" cx="0.4" cy="0.35" r="0.7">
        <stop offset="0" stop-color="#eaffc0"/>
        <stop offset="0.6" stop-color="#7de22a"/>
        <stop offset="1" stop-color="#1f8a14"/>
      </radialGradient>
      <path id="url-arc" d="M 258 1075 A 390 390 0 0 1 590 452"/>
    </defs>
    <circle cx="442" cy="884" r="600" fill="url(#rainbow)"/>
    <ellipse cx="440" cy="962" rx="92" ry="16" fill="#3aa80f" opacity="0.45"/>
    <circle cx="434" cy="779" r="80" fill="url(#orb)"/>
    <text font-family="Arimo, Arial, sans-serif" font-size="44" fill="#7dea12"
          stroke="#ff8a00" stroke-width="1" paint-order="stroke">
      <textPath href="#url-arc" textLength="720" lengthAdjust="spacingAndGlyphs">www.CLOVERTONadoptioncenter.com</textPath>
    </text>
    <rect x="24" y="24" width="654" height="1152" fill="none" stroke="#c9cfd3" stroke-width="3"/>
    <rect x="44" y="44" width="616" height="1112" fill="none" stroke="#c9cfd3" stroke-width="3"/>
  </svg>

  <div class="puppy-photo" role="img" aria-label="Photo of a smiling golden retriever puppy peeking over the edge"></div>

  <h1 class="brand">
    <span class="brand__name">CLOVERTON</span>
    <span class="brand__tagline">Adoption Center</span>
  </h1>

  <p class="person">Maren Hollis</p>

  <p class="contact">
    <span class="contact__name">CLOVERTON</span>
    <span class="contact__phone">555-013-4478</span>
  </p>
</main>
</body>
</html>
```